5Marble Strategy- Logo & Design Work

THIS IS PHASE ONE. I have a stock trading strategy. I need a schematic that shows how it works. I have included sketches. I want the scheme to look like Exhibit A. I want the circles to look like gear shifts in Exhibit B. After this first step is done, we will move on to creating logo like Exhibit C, a second logo like Exhibit D and another Schematic like Exhibit E.

```html
<!DOCTYPE html>
<html lang="en">
<head>
<meta charset="utf-8">
<title>5Marble World Stock Index Strategy – Schematic</title>
<link href="https://fonts.googleapis.com/css2?family=Open+Sans:wght@700&display=swap" rel="stylesheet">
<style>
  :root {
    --green-deep: #1a8b41;
    --green-light: #3fa449;
    --white: #ffffff;
    --blue-deep: #1b67ad;
    --blue-light: #2ba3d1;
  }
  html, body {
    margin: 0;
    padding: 0;
    width: 1200px;
    height: 927px;
    overflow: hidden;
    background: var(--white);
  }
  .schematic {
    display: block;
    width: 1200px;
    height: 927px;
  }
  .orbit {
    fill: none;
    stroke: var(--green-deep);
    stroke-width: 36;
  }
  .gear-mask { fill: var(--white); }
  .gear-teeth {
    fill: none;
    stroke: var(--green-light);
    stroke-width: 26;
    stroke-dasharray: 40 39.85;
  }
  .gear-body { fill: url(#gearShade); }
  .gear-face {
    fill: var(--green-deep);
    stroke: var(--white);
    stroke-width: 3;
  }
  .gear-label {
    font-family: "Open Sans", sans-serif;
    font-weight: 700;
    font-size: 29px;
    fill: var(--white);
    text-anchor: middle;
  }
  .gear-note {
    font-family: "Open Sans", sans-serif;
    font-weight: 700;
    font-size: 15px;
    fill: var(--white);
    text-anchor: middle;
  }
  .flow-arrow { fill: url(#arrowShade); }
</style>
</head>
<body>
<svg class="schematic" viewBox="0 0 2000 1545" xmlns="http://www.w3.org/2000/svg" role="img" aria-label="5Marble World Stock Index Strategy schematic">
  <defs>
    <radialGradient id="gearShade">
      <stop offset="0.7" stop-color="#1a8b41"/>
      <stop offset="1" stop-color="#3fa449"/>
    </radialGradient>
    <linearGradient id="arrowShade" x1="0" y1="0" x2="1" y2="1">
      <stop offset="0" stop-color="#1b67ad"/>
      <stop offset="0.55" stop-color="#2ba3d1"/>
      <stop offset="1" stop-color="#1b67ad"/>
    </linearGradient>
    <g id="gear">
      <circle class="gear-teeth" r="152.5"/>
      <circle class="gear-body" r="142"/>
      <circle class="gear-face" r="113"/>
    </g>
    <path id="arrow" d="M650,528 C655,600 700,632 775,645 L773,625 L848,692 L748,716 L765,697 C688,678 645,620 650,528 Z"/>
  </defs>

  <circle class="orbit" cx="1000" cy="772" r="562"/>

  <g class="gear-masks">
    <circle class="gear-mask" cx="577" cy="371" r="172"/>
    <circle class="gear-mask" cx="1423" cy="371" r="172"/>
    <circle class="gear-mask" cx="577" cy="1173" r="172"/>
    <circle class="gear-mask" cx="1423" cy="1173" r="172"/>
  </g>

  <g class="flow-arrows">
    <use class="flow-arrow" href="#arrow"/>
    <use class="flow-arrow" href="#arrow" transform="translate(2000,0) scale(-1,1)"/>
    <use class="flow-arrow" href="#arrow" transform="translate(0,1544) scale(1,-1)"/>
    <use class="flow-arrow" href="#arrow" transform="translate(2000,1544) scale(-1,-1)"/>
  </g>

  <g class="gear gear-rebalance" transform="translate(577,371)">
    <use href="#gear"/>
    <text class="gear-label" y="-26">Rebalance</text>
    <text class="gear-label" y="7">Annually</text>
    <text class="gear-note" y="41">LOREN IPSUM</text>
    <text class="gear-note" y="59">LOREN</text>
  </g>

  <g class="gear gear-trend" transform="translate(1423,371)">
    <use href="#gear"/>
    <text class="gear-label" y="-26">Trend</text>
    <text class="gear-label" y="7">33%</text>
    <text class="gear-label" y="40">Allocation</text>
  </g>

  <g class="gear gear-buyhold" transform="translate(577,1173)">
    <use href="#gear"/>
    <text class="gear-label" y="-24">Buy &amp; Hold</text>
    <text class="gear-label" y="9">33%</text>
    <text class="gear-label" y="42">Allocation</text>
  </g>

  <g class="gear gear-tactical" transform="translate(1423,1173)">
    <use href="#gear"/>
    <text class="gear-label" y="-24">Tactical</text>
    <text class="gear-label" y="9">33%</text>
    <text class="gear-label" y="42">Allocation</text>
  </g>

  <g class="gear gear-core" transform="translate(1000,772)">
    <use href="#gear"/>
    <text class="gear-label" y="-41">5Marble</text>
    <text class="gear-label" y="-8">World Stock</text>
    <text class="gear-label" y="25">Index</text>
    <text class="gear-label" y="58">Strategy</text>
  </g>
</svg>
</body>
</html>
```